Business Card Design

We are a law firm which provides services to creditors.....we do collection litigation. I am wide open on suggestions. I was thinking of a square card? Alternatively, a vertically oriented standard card or a folded card.....something unique. I would like to use my firm logo and beyond that, I am open for any and all suggestions. I'm uncertain if the complete log is uploaded? If not, please let me email it to you.

Industry/Entity Type

Law Firm

Contact Information for Business Card

Harte, Quill & Dorsey, P.C.
Tom Dorsey, Lawyer
4187 W Cobbler Ave
Oklahoma City, OK 73116
tdorsey@HqdLegal.com
www.HqdLegal.com
mobile: 405-555-0182

```html
<!DOCTYPE html>
<html lang="en">
<head>
<meta charset="utf-8">
<title>Harte, Quill &amp; Dorsey, P.C. — Business Card</title>
<link rel="stylesheet" href="https://fonts.googleapis.com/css2?family=Arimo:wght@400&display=swap">
<style>
  :root {
    --backdrop: #e9e6e1;
    --card-black: #0b0b0b;
    --card-sheen: #1c1c1c;
    --gold: #c9a23c;
  }
  * { margin: 0; padding: 0; box-sizing: border-box; }
  html, body {
    width: 1200px;
    height: 892px;
    overflow: hidden;
    background: var(--backdrop);
  }
  .canvas {
    width: 1200px;
    height: 892px;
    display: flex;
    align-items: center;
    justify-content: center;
  }
  .business-card {
    position: relative;
    width: 1000px;
    height: 571px;
    background: linear-gradient(125deg, var(--card-sheen) 0%, var(--card-black) 45%, var(--card-black) 100%);
    border-radius: 6px;
    box-shadow: 0 10px 30px rgba(0,0,0,0.25);
    font-family: "Arimo", Arial, sans-serif;
    color: var(--gold);
    display: flex;
    flex-direction: column;
    align-items: center;
    justify-content: center;
    gap: 44px;
    padding-bottom: 20px;
  }
  .firm-mark {
    display: flex;
    align-items: center;
    justify-content: center;
    gap: 16px;
    font-size: 24px;
    letter-spacing: 0.12em;
    text-transform: uppercase;
    white-space: nowrap;
  }
  .firm-mark-dot {
    width: 56px;
    height: 56px;
    border-radius: 50%;
    background: var(--gold);
    flex: none;
  }
  .firm-name {
    font-size: 54px;
    letter-spacing: 0.01em;
    white-space: nowrap;
    text-align: center;
  }
</style>
</head>
<body>
  <main class="canvas">
    <section class="business-card" aria-label="Business card front">
      <div class="firm-mark">
        <span class="firm-mark-dot" aria-hidden="true"></span>
        <span class="firm-mark-name">Harte Quill Dorsey</span>
      </div>
      <p class="firm-name">Harte, Quill &amp; Dorsey, P.C.</p>
    </section>
  </main>
</body>
</html>
```